Flyer / Mailer for Business Debt Relief Business - Tillbrook Partners 6" x 11"

We need a 6" x 11" double sided flyer. This will be sent out to potential customers with high interest business loans. We would like the design to coordinate with the colors of our logo. I have included a mock up that we sketched out. I have also included a file of a mailer we received that we would like to use as a template (not colors or fonts, just set up). I have also included an .ai file of our logo.

```html
<!DOCTYPE html>
<html lang="en">
<head>
<meta charset="utf-8">
<title>Tillbrook Partners – Debt Relief Mailer</title>
<link href="https://fonts.googleapis.com/css2?family=Bebas+Neue&family=Ubuntu:wght@400;500&display=swap" rel="stylesheet">
<style>
  :root {
    --page: #e4e4e4;
    --paper: #f3f3f3;
    --paper-light: #f8f8f8;
    --brand-blue: #1a73bd;
    --deep-blue: #0b3f8c;
    --sky-blue: #1aa0dc;
    --brand-green: #8dc63f;
    --lime: #a8d13c;
    --ink: #4a4a4a;
    --white: #ffffff;
  }
  * { box-sizing: border-box; margin: 0; padding: 0; }
  html, body { width: 1090px; height: 1200px; overflow: hidden; }
  body {
    background: var(--page);
    font-family: "Ubuntu", sans-serif;
    position: relative;
  }
  h1, h2 { font-weight: 400; }
  .card {
    position: absolute;
    left: 20px;
    width: 1050px;
    height: 573px;
    background: var(--paper);
    overflow: hidden;
    box-shadow: 0 2px 6px rgba(0,0,0,.18);
  }
  .card--front { top: 20px; }
  .card--back { top: 607px; }
  .card__art { position: absolute; inset: 0; width: 100%; height: 100%; }
  .abs { position: absolute; white-space: nowrap; }

  .headline {
    font-family: "Bebas Neue", sans-serif;
    color: var(--brand-blue);
    font-size: 35px;
    line-height: 41px;
  }
  .subline { color: var(--brand-green); font-size: 17px; line-height: 23px; }

  .wordmark { display: flex; align-items: center; gap: 12px; color: var(--ink); }
  .wordmark__square { width: 22px; height: 22px; background: var(--brand-green); flex: none; }
  .wordmark__name { font-size: 22px; font-weight: 400; letter-spacing: 1px; text-transform: uppercase; }
  .wordmark--stacked { flex-direction: column; gap: 14px; width: 220px; }
  .wordmark--stacked .wordmark__square { width: 52px; height: 52px; }
  .wordmark--stacked .wordmark__name { font-size: 19px; letter-spacing: .6px; }
  .wordmark--large .wordmark__square { width: 34px; height: 34px; }
  .wordmark--large .wordmark__name { font-size: 32px; }

  .panel-title { color: var(--white); font-size: 22px; }
  .benefits { list-style: none; color: var(--white); font-size: 18px; }
  .benefits li { display: flex; align-items: center; gap: 11px; height: 25.3px; }
  .benefits svg { width: 14px; height: 14px; flex: none; }

  .cta { color: var(--brand-blue); font-weight: 500; font-size: 18px; }
  .contacts { display: flex; gap: 24px; font-size: 15px; color: var(--ink); }
  .contacts span { display: flex; align-items: center; gap: 9px; }
  .contacts svg { width: 14px; height: 14px; }
  .contacts--light { color: var(--white); font-size: 16px; }

  .phone { display: flex; align-items: center; gap: 14px; font-size: 25px; font-weight: 500; }
  .phone svg { width: 26px; height: 26px; }
  .phone--light { color: var(--white); }
  .phone--blue { color: var(--brand-blue); }

  .back-headline {
    font-family: "Bebas Neue", sans-serif;
    color: var(--brand-green);
    font-size: 29px;
    line-height: 32px;
  }
  .back-body { color: var(--white); font-size: 17.5px; line-height: 25px; }
  .back-cta { color: var(--brand-blue); font-weight: 500; font-size: 18px; line-height: 24px; }
  .address { color: var(--ink); font-size: 16px; line-height: 25px; }
</style>
</head>
<body>

<!-- Front side -->
<section class="card card--front">
  <svg class="card__art" viewBox="0 0 1100 600" preserveAspectRatio="none">
    <defs>
      <linearGradient id="jarPhoto" x1="0" y1="0" x2="1" y2="1">
        <stop offset="0" stop-color="#5f7f2a"/>
        <stop offset=".45" stop-color="#9a8a55"/>
        <stop offset="1" stop-color="#4b3424"/>
      </linearGradient>
      <linearGradient id="frontPanel" x1="0" y1="0" x2="1" y2="0">
        <stop offset="0" stop-color="#1a9ad6"/>
        <stop offset="1" stop-color="#0a3a86"/>
      </linearGradient>
      <linearGradient id="frontBand" x1="0" y1="0" x2="1" y2="0">
        <stop offset="0" stop-color="#8dc63f"/>
        <stop offset="1" stop-color="#a8d13c"/>
      </linearGradient>
      <linearGradient id="advisorPhoto" x1="0" y1="0" x2="0" y2="1">
        <stop offset="0" stop-color="#1f4f96"/>
        <stop offset="1" stop-color="#1b2236"/>
      </linearGradient>
    </defs>
    <polygon points="0,0 465,0 410,516 0,516" fill="url(#jarPhoto)" role="img" aria-label="Photo of a seedling growing from a glass jar of coins on a wooden table"/>
    <polygon points="455,193 1100,193 1100,516 418,516" fill="url(#frontPanel)"/>
    <polygon points="590,526 900,526 900,600 560,600" fill="url(#frontBand)"/>
    <rect x="900" y="258" width="200" height="342" fill="url(#advisorPhoto)" role="img" aria-label="Photo of a smiling consultant in a dark suit with arms crossed"/>
  </svg>

  <h1 class="abs headline" style="left:437px; top:34px;">Helping businesses focus<br>on what matters!</h1>
  <p class="abs subline" style="left:437px; top:120px;">We understand that merchant cash<br>advance loans can be a burden on your business</p>

  <div class="abs wordmark wordmark--stacked" style="left:826px; top:36px;">
    <span class="wordmark__square"></span>
    <span class="wordmark__name">Tillbrook Partners</span>
  </div>

  <h2 class="abs panel-title" style="left:437px; top:198px;">Over whelmed by daily/weekly payments? WE CAN HELP!</h2>
  <ul class="abs benefits" style="left:437px; top:234px;">
    <li><svg viewBox="0 0 14 14"><circle cx="7" cy="7" r="7" fill="#8dc63f"/><path d="M5.5 4l3 3-3 3" stroke="#fff" stroke-width="1.8" fill="none"/></svg>This is not loan, we are not lenders!</li>
    <li><svg viewBox="0 0 14 14"><circle cx="7" cy="7" r="7" fill="#8dc63f"/><path d="M5.5 4l3 3-3 3" stroke="#fff" stroke-width="1.8" fill="none"/></svg>Improve your business cash flow immediately</li>
    <li><svg viewBox="0 0 14 14"><circle cx="7" cy="7" r="7" fill="#8dc63f"/><path d="M5.5 4l3 3-3 3" stroke="#fff" stroke-width="1.8" fill="none"/></svg>Move payments to one monthly amount</li>
    <li><svg viewBox="0 0 14 14"><circle cx="7" cy="7" r="7" fill="#8dc63f"/><path d="M5.5 4l3 3-3 3" stroke="#fff" stroke-width="1.8" fill="none"/></svg>Reduce the amount you are paying out monthly</li>
    <li><svg viewBox="0 0 14 14"><circle cx="7" cy="7" r="7" fill="#8dc63f"/><path d="M5.5 4l3 3-3 3" stroke="#fff" stroke-width="1.8" fill="none"/></svg>Strategic alternatives to his interest loans</li>
    <li><svg viewBox="0 0 14 14"><circle cx="7" cy="7" r="7" fill="#8dc63f"/><path d="M5.5 4l3 3-3 3" stroke="#fff" stroke-width="1.8" fill="none"/></svg>Fast, confidential business debit relief</li>
    <li><svg viewBox="0 0 14 14"><circle cx="7" cy="7" r="7" fill="#8dc63f"/><path d="M5.5 4l3 3-3 3" stroke="#fff" stroke-width="1.8" fill="none"/></svg>No-obliseton consultation</li>
    <li><svg viewBox="0 0 14 14"><circle cx="7" cy="7" r="7" fill="#8dc63f"/><path d="M5.5 4l3 3-3 3" stroke="#fff" stroke-width="1.8" fill="none"/></svg>Absolutely no credit pulls</li>
    <li><svg viewBox="0 0 14 14"><circle cx="7" cy="7" r="7" fill="#8dc63f"/><path d="M5.5 4l3 3-3 3" stroke="#fff" stroke-width="1.8" fill="none"/></svg>No collateral, no financial</li>
  </ul>

  <p class="abs cta" style="left:32px; top:519px;">CALL NOW FOR FREE CONSULTATION WITH OUR EXPERTS</p>
  <div class="abs contacts" style="left:34px; top:550px;">
    <span><svg viewBox="0 0 14 14"><circle cx="7" cy="7" r="6" fill="none" stroke="#777" stroke-width="1.2"/><path d="M1 7h12M7 1v12M3 3.5q4 2 8 0M3 10.5q4-2 8 0" stroke="#777" stroke-width=".9" fill="none"/></svg>www.tillbrookpartners.com</span>
    <span><svg viewBox="0 0 14 14"><circle cx="7" cy="7" r="6" fill="none" stroke="#777" stroke-width="1.2"/><rect x="3.5" y="4.8" width="7" height="4.6" fill="#777"/></svg>info@tillbrookpartners.com</span>
  </div>

  <div class="abs phone phone--light" style="left:598px; top:535px;">
    <svg viewBox="0 0 26 26"><circle cx="13" cy="13" r="11.5" fill="none" stroke="#fff" stroke-width="2"/><path d="M9 7.5l2.3-.4 1.2 3-1.5 1.2q1.2 2.6 3.6 3.7l1.3-1.5 3 1.3-.4 2.3q-4.2.6-7.3-2.5T9 7.5z" fill="#fff"/></svg>
    888-555-0142
  </div>
</section>

<!-- Back side -->
<section class="card card--back">
  <svg class="card__art" viewBox="0 0 1100 600" preserveAspectRatio="none">
    <defs>
      <linearGradient id="backPanel" x1="0" y1="0" x2="1" y2="0">
        <stop offset="0" stop-color="#1aa6e0"/>
        <stop offset="1" stop-color="#0b3f8c"/>
      </linearGradient>
      <linearGradient id="backBand" x1="0" y1="0" x2="1" y2="0">
        <stop offset="0" stop-color="#8dc63f"/>
        <stop offset=".75" stop-color="#a8d13c"/>
        <stop offset="1" stop-color="#5ea53a"/>
      </linearGradient>
      <linearGradient id="teamPhoto" x1="0" y1="0" x2="1" y2="1">
        <stop offset="0" stop-color="#2f6fb8"/>
        <stop offset="1" stop-color="#16417f"/>
      </linearGradient>
    </defs>
    <polygon points="0,0 490,0 510,188 0,188" fill="#f8f8f8"/>
    <line x1="490" y1="0" x2="550" y2="600" stroke="#d4d4d4" stroke-width="3"/>
    <polygon points="0,188 510,188 535,488 0,488" fill="url(#backPanel)"/>
    <polygon points="0,493 530,493 550,600 0,600" fill="url(#backBand)"/>
    <polygon points="320,238 514,238 532,455 320,455" fill="url(#teamPhoto)" role="img" aria-label="Photo of two smiling business professionals, one holding a tablet"/>
    <polygon points="320,455 535,455 545,535 285,535" fill="#ffffff"/>
  </svg>

  <div class="abs wordmark wordmark--large" style="left:43px; top:72px;">
    <span class="wordmark__square"></span>
    <span class="wordmark__name">Tillbrook Partners</span>
  </div>

  <p class="abs address" style="left:506px; top:32px;">418 Meridian Ave<br>Fairhaven, Harlow County 75021</p>

  <h2 class="abs back-headline" style="left:29px; top:214px;">Strategic debit relief for<br>businesses of all sizes</h2>
  <p class="abs back-body" style="left:30px; top:294px;">Stop taking out loans to<br>pay off other loans.<br>Take back your business’s<br>cash flow, and focus on<br>what matters.</p>

  <div class="abs phone phone--blue" style="left:314px; top:469px;">
    <svg viewBox="0 0 26 26"><circle cx="13" cy="13" r="11.5" fill="none" stroke="#1a73bd" stroke-width="2"/><path d="M9 7.5l2.3-.4 1.2 3-1.5 1.2q1.2 2.6 3.6 3.7l1.3-1.5 3 1.3-.4 2.3q-4.2.6-7.3-2.5T9 7.5z" fill="#1a73bd"/></svg>
    888-555-0142
  </div>

  <p class="abs back-cta" style="left:29px; top:480px;">CALL NOW FOR FREE<br>CONSULTATION!</p>
  <div class="abs contacts contacts--light" style="left:29px; top:536px;">
    <span><svg viewBox="0 0 14 14"><circle cx="7" cy="7" r="6" fill="none" stroke="#fff" stroke-width="1.2"/><path d="M1 7h12M7 1v12M3 3.5q4 2 8 0M3 10.5q4-2 8 0" stroke="#fff" stroke-width=".9" fill="none"/></svg>www.tillbrookpartners.com</span>
    <span><svg viewBox="0 0 14 14"><circle cx="7" cy="7" r="6" fill="none" stroke="#fff" stroke-width="1.2"/><rect x="3.5" y="4.8" width="7" height="4.6" fill="#fff"/></svg>info@tillbrookpartners.com</span>
  </div>
</section>

</body>
</html>
```